Brivolan - presentation for a remote DBA team offering data platform management

We need a website design for wordpress site called Brivolan.cz
We deliver remote database and data platform administration and development, oversee the database administrators, consult and train the personnel responsible for the database operations. The website should include several sections, home page with graphics elements supporting the name and service - remote dba work; blog section; service introduction and description, team introduction and description, download section for documents, presentations etc.

Target Market(s)

small and medium business companies requiring remote DBA service

Number of Pages Required

3 page

Font styles to use
Sans Serif

Colors

Designer to choose colors to be used in the design.

Requirements
Must have
• The website should have several sections to introduce the services, blog, team introduction, downloads

```html
<!DOCTYPE html>
<html lang="en">
<head>
<meta charset="utf-8">
<title>Brivolan – Remote DBA Team</title>
<link href="https://fonts.googleapis.com/css2?family=Lato:ital,wght@0,300;0,400;0,700;0,900;1,400&family=Montserrat:wght@300;400;500;600;700&family=Oswald:wght@500;600&display=swap" rel="stylesheet">
<style>
:root{
  --blue:#0d57a7;
  --blue-dark:#0a4688;
  --green:#6aa62a;
  --green-dark:#5a9120;
  --ink:#1d1d1f;
  --text:#3a3a3a;
  --muted:#8a8a8a;
  --light:#f3f3f3;
  --line:#dcdcdc;
  --footer:#1e1e1f;
  --white:#ffffff;
}
*{box-sizing:border-box;margin:0;padding:0}
html,body{width:1200px;height:3974px;overflow:hidden}
body{font-family:"Lato",Arial,sans-serif;color:var(--text);background:var(--white);position:relative}
.abs{position:absolute}
section,header,footer{position:absolute;left:0;width:1200px;overflow:hidden}

/* header */
.site-header{top:0;height:88px;background:var(--white);border-bottom:1px solid #e6e6e6}
.topbar{position:absolute;left:175px;top:6px;width:850px;height:22px;font-size:11px;color:#555;display:flex;align-items:center}
.topbar .item{display:flex;align-items:center;gap:6px;margin-right:22px}
.topbar svg{width:12px;height:12px}
.topbar .socials{margin-left:auto;display:flex;gap:9px;align-items:center}
.sq{width:13px;height:13px;border:1.5px solid #888;border-radius:2px;display:inline-block}
.lang{display:flex;align-items:center;gap:4px;margin-left:10px;font-size:10px}
.lang i{width:11px;height:11px;border-radius:50%;background:#c8202f;display:inline-block}
.navrow{position:absolute;left:175px;top:34px;width:850px;height:46px;display:flex;align-items:center}
.brand{display:flex;align-items:center;gap:10px;font-family:"Montserrat",sans-serif;font-weight:700;font-size:20px;color:var(--blue);letter-spacing:.5px}
.brand .mark{width:26px;height:26px;background:var(--blue);border-radius:3px}
.mainnav{margin-left:auto;display:flex;align-items:center;font-size:13px;color:#333;font-family:"Montserrat",sans-serif}
.mainnav a{color:inherit;text-decoration:none;padding:0 13px}
.mainnav .home{width:36px;height:26px;display:flex;align-items:center;justify-content:center;padding:0}
.mainnav .home svg{width:18px;height:18px}
.mainnav .small{font-size:10px}
.search{width:120px;height:24px;border:1px solid var(--line);margin-left:10px;display:flex;align-items:center;justify-content:space-between;padding:0 6px;font-size:10px;color:#999}
.search svg{width:12px;height:12px}

/* hero */
.hero{top:88px;height:522px;background:radial-gradient(circle at 78% 40%,#3a3226 0%,#1a1713 35%,#0c0b0a 70%);border-bottom:5px solid var(--blue)}
.hero .visual{position:absolute;left:520px;top:0;width:680px;height:517px;background:radial-gradient(ellipse at 55% 45%,rgba(214,168,110,.45) 0%,rgba(120,90,60,.25) 35%,rgba(0,0,0,0) 70%)}
.hero h1{position:absolute;left:175px;top:168px;font-family:"Oswald",sans-serif;font-weight:600;font-size:38px;letter-spacing:1px;color:var(--white)}
.hero .lead{position:absolute;left:175px;top:246px;font-family:"Montserrat",sans-serif;font-size:19px;line-height:28px;color:var(--white);font-weight:500}
.btn-split{display:flex;height:38px;font-family:"Montserrat",sans-serif;font-size:12px;color:var(--white)}
.btn-split .label{background:var(--blue);display:flex;align-items:center;padding:0 16px}
.btn-split .go{background:var(--green);width:40px;display:flex;align-items:center;justify-content:center}
.btn-split .go svg{width:10px;height:10px}
.hero .btn-split{position:absolute;left:175px;top:332px}
.mouse{position:absolute;left:589px;top:428px;width:22px;height:36px;border:2px solid var(--white);border-radius:11px}
.mouse::after{content:"";position:absolute;left:8px;top:6px;width:2px;height:8px;background:var(--white);border-radius:1px}

/* section titles */
.sec-title{position:absolute;left:0;width:1200px;text-align:center;font-family:"Montserrat",sans-serif;font-weight:300;font-size:34px;color:#444}
.sec-title b{font-weight:700;color:var(--ink)}
.sec-title b .g{color:var(--green)}
.sec-sub{position:absolute;left:250px;width:700px;text-align:center;font-size:14px;line-height:21px;color:var(--muted)}

/* about */
.about{top:610px;height:622px;background:linear-gradient(180deg,#f7f7f7,#efefef)}
.about .kicker{position:absolute;left:175px;top:196px;font-family:"Montserrat",sans-serif;font-weight:700;font-size:14px;color:var(--blue)}
.about .intro{position:absolute;left:175px;top:230px;width:430px;font-size:16px;line-height:24px;color:#222}
.about .fine{position:absolute;left:175px;width:430px;font-size:11px;line-height:17px;color:var(--muted)}
.about .btn-split{position:absolute;left:175px;top:537px}
.features{position:absolute;left:654px;top:193px;width:372px;height:376px}
.feat{position:absolute;width:174px;height:174px;display:flex;flex-direction:column;align-items:center;justify-content:center;text-align:center;font-family:"Montserrat",sans-serif;font-size:11px;line-height:15px;text-transform:uppercase;color:#333;background:var(--white);border:1px solid var(--line)}
.feat svg{width:34px;height:34px;margin-bottom:14px}
.feat.blue{background:var(--blue);color:var(--white);border-color:var(--blue)}
.feat.green{background:var(--green);color:var(--white);border-color:var(--green)}
.feat.f1{left:0;top:0}.feat.f2{left:198px;top:0}.feat.f3{left:0;top:202px}.feat.f4{left:198px;top:202px}
.hub{position:absolute;left:150px;top:152px;width:72px;height:72px;border-radius:50%;background:var(--white);display:flex;align-items:center;justify-content:center}
.hub span{width:50px;height:50px;border-radius:50%;background:var(--blue);display:flex;align-items:center;justify-content:center}
.hub svg{width:24px;height:24px}

/* products */
.products{top:1232px;height:490px;background:var(--white)}
.cards{position:absolute;left:175px;top:204px;width:851px;display:flex;gap:29px}
.card{width:191px}
.card .ph{height:196px}
.card .bar{height:32px;display:flex;align-items:center;justify-content:center;font-family:"Montserrat",sans-serif;font-weight:600;font-size:12px;color:var(--white);text-transform:uppercase}
.card .bar.blue{background:var(--blue)}.card .bar.green{background:var(--green)}
.circ-arrow{position:absolute;width:20px;height:20px;border:1px solid #bbb;border-radius:50%;display:flex;align-items:center;justify-content:center}
.circ-arrow svg{width:8px;height:8px}

/* experience */
.experience{top:1722px;height:304px;background:linear-gradient(90deg,#2b2b2b,#555 30%,#4a4744 60%,#2a2825)}
.experience .ph{position:absolute;inset:0;background:linear-gradient(180deg,rgba(0,0,0,.25),rgba(0,0,0,.45))}
.experience h2{position:absolute;left:0;width:1200px;top:80px;text-align:center;font-family:"Montserrat",sans-serif;font-weight:500;font-size:26px;color:var(--white);letter-spacing:.5px}
.experience .tag{position:absolute;left:0;width:1200px;top:125px;text-align:center;font-family:"Montserrat",sans-serif;font-size:14px;color:var(--green);text-transform:uppercase;letter-spacing:.5px}
.experience .phone{position:absolute;left:388px;top:192px;font-family:"Montserrat",sans-serif;font-size:28px;color:var(--white)}
.btn-outline{position:absolute;left:622px;top:190px;width:181px;height:42px;border:1px solid rgba(255,255,255,.8);display:flex;align-items:center;font-family:"Montserrat",sans-serif;font-size:13px;color:var(--white)}
.btn-outline .label{flex:1;padding-left:26px}
.btn-outline .go{width:42px;height:100%;border-left:1px solid rgba(255,255,255,.8);display:flex;align-items:center;justify-content:center}
.btn-outline svg{width:10px;height:10px}

/* blog */
.blog{top:2026px;height:544px;background:#f6f6f6}
.posts{position:absolute;left:175px;top:204px;width:851px;display:flex;gap:20px}
.post{width:270px;border-left:4px solid #cfcfcf;background:var(--white)}
.post .ph{height:132px}
.post .body{padding:10px 12px 12px}
.post h3{font-family:"Montserrat",sans-serif;font-weight:600;font-size:11px;color:var(--blue);text-transform:uppercase}
.post .date{font-size:9px;color:#555;margin-top:5px;display:flex;align-items:center;gap:4px;font-weight:700}
.post .date i{width:8px;height:8px;border:1px solid var(--blue);display:inline-block}
.post p{font-size:9.5px;line-height:13px;color:var(--muted);margin-top:6px}
.post .more{font-size:9px;font-weight:700;color:var(--green);margin-top:6px}
.dots{position:absolute;left:580px;top:481px;display:flex;gap:6px}
.dots i{width:8px;height:8px;border-radius:50%;border:1px solid #999;display:block}
.dots i.on{background:var(--blue);border-color:var(--blue)}

/* testimonial */
.testimonial{top:2570px;height:344px;background:linear-gradient(180deg,#fafafa,#eeeeee)}
.testimonial .quote{position:absolute;left:578px;top:36px;width:44px;height:36px}
.testimonial blockquote{position:absolute;left:300px;width:600px;top:98px;text-align:center;font-style:italic;font-size:16px;line-height:23px;color:#555}
.testimonial .arr{position:absolute;top:128px;width:20px;height:20px}
.avatar{position:absolute;left:575px;top:200px;width:50px;height:50px;border-radius:50%;border:3px solid var(--white);background:radial-gradient(circle at 50% 40%,#d9b8a0,#6e6a66)}
.testimonial .name{position:absolute;left:0;width:1200px;top:266px;text-align:center;font-size:13px;color:var(--blue);font-weight:700}
.testimonial .role{position:absolute;left:0;width:1200px;top:286px;text-align:center;font-size:12px;color:#666}

/* team */
.team{top:2914px;height:318px;background:var(--white)}
.member{position:absolute;left:175px;top:26px;width:851px;height:257px;border:3px solid var(--blue);border-left:none;background:var(--white)}
.member .ph{position:absolute;left:0;top:-3px;width:256px;height:257px;background:linear-gradient(160deg,#8c9196,#5a5f65 60%,#3d4045)}
.member h3{position:absolute;left:310px;top:28px;font-family:"Montserrat",sans-serif;font-weight:500;font-size:20px;color:var(--ink);letter-spacing:.5px}
.member .pos{position:absolute;left:310px;top:58px;font-size:13px;color:var(--green);font-weight:700}
.member p{position:absolute;left:310px;top:88px;width:510px;font-size:11px;line-height:16px;color:var(--muted)}
.member .contact{position:absolute;left:310px;top:148px;border-left:4px solid var(--green);padding-left:10px;font-size:10.5px;line-height:16px;color:#555}
.member .soc{position:absolute;left:310px;top:200px;display:flex;gap:6px}
.member .soc i{width:18px;height:18px;background:var(--ink);display:block}
.member .pager{position:absolute;right:26px;top:198px;display:flex;gap:6px}
.member .pager span{width:22px;height:22px;border:1px solid var(--blue);display:flex;align-items:center;justify-content:center}
.member .pager svg{width:8px;height:8px}

/* downloads / discussion */
.downloads{top:3232px;height:402px}
.dl-side{position:absolute;left:0;top:0;width:600px;height:402px;background:var(--blue)}
.dl{position:absolute;left:271px;width:200px;text-align:center;color:var(--white);font-family:"Montserrat",sans-serif;font-weight:700;font-size:14px}
.dl svg{width:70px;height:86px;display:block;margin:0 auto 12px}
.talk-side{position:absolute;left:600px;top:0;width:600px;height:402px;background:var(--green)}
.talk-side h2{position:absolute;left:54px;top:50px;font-family:"Montserrat",sans-serif;font-weight:400;font-size:24px;color:var(--white)}
.field{position:absolute;height:32px;background:var(--white);font-size:10px;color:#888;padding:9px 10px}
.submit{position:absolute;left:54px;top:309px;width:158px;height:40px;border:1px solid var(--white);display:flex;align-items:center;font-family:"Montserrat",sans-serif;font-size:12px;color:var(--white)}
.submit .label{flex:1;padding-left:24px}
.submit .go{width:40px;height:100%;border-left:1px solid var(--white);display:flex;align-items:center;justify-content:center}
.submit svg{width:10px;height:10px}

/* footer */
.site-footer{top:3634px;height:340px;background:var(--footer);color:#bdbdbd}
.site-footer .brand{position:absolute;left:175px;top:76px;color:var(--white)}
.site-footer .brand .mark{background:var(--white)}
.f-phone{position:absolute;left:175px;top:140px;font-family:"Montserrat",sans-serif;font-size:22px;color:var(--white)}
.f-addr{position:absolute;left:175px;top:176px;font-size:12px;line-height:17px;color:#9a9a9a}
.f-head{position:absolute;top:66px;font-family:"Montserrat",sans-serif;font-size:18px;color:var(--white)}
.f-head::after{content:"";position:absolute;left:0;top:30px;width:28px;height:2px;background:var(--green)}
.f-list{position:absolute;top:120px;font-size:11px;line-height:21px;color:#9a9a9a;list-style:none}
.f-news{position:absolute;left:813px;top:120px;font-size:11px;color:#9a9a9a}
.f-email{position:absolute;left:813px;top:148px;width:212px;height:30px;background:#111;display:flex;align-items:center;font-size:10px;color:#777;padding-left:10px}
.f-email span{margin-left:auto;width:40px;height:30px;background:var(--blue);display:flex;align-items:center;justify-content:center}
.f-email svg{width:14px;height:14px}
.f-soc{position:absolute;left:813px;top:194px;display:flex;gap:8px}
.f-soc i{width:20px;height:20px;border:1px solid #888;border-radius:50%;display:block}
.f-bottom{position:absolute;left:175px;top:278px;width:850px;border-top:1px solid #3a3a3a;padding-top:22px;display:flex;justify-content:space-between;font-size:10px;color:#8a8a8a}
.to-top{position:absolute;left:1148px;top:266px;width:24px;height:44px;border-radius:12px;background:var(--green);display:flex;align-items:center;justify-content:center}
.to-top svg{width:10px;height:10px}
</style>
</head>
<body>

<header class="site-header">
  <div class="topbar">
    <div class="item"><svg viewBox="0 0 12 12"><rect x="1" y="2.5" width="10" height="7" fill="none" stroke="#0d57a7"/><path d="M1 2.5l5 4 5-4" fill="none" stroke="#0d57a7"/></svg>info@brivolan.cz</div>
    <div class="item"><svg viewBox="0 0 12 12"><path d="M3 1l2 2.5-1.2 1.3a7 7 0 0 0 3.4 3.4L8.5 7 11 9l-1.5 2A9 9 0 0 1 1 2.5z" fill="#6aa62a"/></svg>1800.555.0142</div>
    <div class="socials"><i class="sq"></i><i class="sq"></i><i class="sq"></i><i class="sq"></i><i class="sq"></i><span class="lang"><i></i>EN</span></div>
  </div>
  <div class="navrow">
    <div class="brand"><span class="mark"></span>BRIVOLAN</div>
    <nav class="mainnav">
      <a class="home" href="#"><svg viewBox="0 0 18 18"><path d="M2 9l7-6 7 6h-2v6h-4v-4H8v4H4V9z" fill="#6aa62a"/></svg></a>
      <a href="#">About</a>
      <a href="#">Products &amp; Services</a>
      <a href="#">Team</a>
      <a href="#" class="small">Downloads</a>
      <a href="#">Contact</a>
      <div class="search">Search...<svg viewBox="0 0 12 12"><circle cx="5" cy="5" r="3.5" fill="none" stroke="#6aa62a" stroke-width="1.5"/><path d="M7.5 7.5l3 3" stroke="#6aa62a" stroke-width="1.5"/></svg></div>
    </nav>
  </div>
</header>

<section class="hero">
  <div class="visual" role="img" aria-label="Glowing network globe of connected data points"></div>
  <h1>HANDLE DATA WIRELESSLEY</h1>
  <p class="lead">Professionally manage your<br>DATABASE</p>
  <div class="btn-split"><span class="label">Request Free Qoute</span><span class="go"><svg viewBox="0 0 10 10"><path d="M3 1l4 4-4 4" fill="none" stroke="#fff" stroke-width="1.6"/></svg></span></div>
  <div class="mouse"></div>
</section>

<section class="about">
  <h2 class="sec-title" style="top:54px">About <b>BRIVOLAN</b></h2>
  <p class="sec-sub" style="top:104px">Performance Tuning and Disaster Recovery deployment using smart computing and proactive tasks</p>
  <div class="kicker">WELCOME TO OUR FIRM</div>
  <p class="intro">Technical writing. Your business requires it – whether it's online help, product documentation, eLearning, or something else entirely, you need it done well. That's where BRIVOLAN comes in.</p>
  <p class="fine" style="top:383px">Sed quia consequuntur magni dolores eos qui ratione voluptatem sequi nesciunt. Neque porro quisquam est qui dolorem ipsum quia dolor sit amet, consectetur, adipisci velit, sed quia non numquam eius modi tempora incidunt.</p>
  <p class="fine" style="top:450px">Neque porro quisquam est, qui dolorem ipsum quia dolor sit amet, consectetur, adipisci velit sed quia non numquam eius modi tempora.</p>
  <div class="btn-split"><span class="label">Start a Discussion</span><span class="go"><svg viewBox="0 0 10 10"><path d="M3 1l4 4-4 4" fill="none" stroke="#fff" stroke-width="1.6"/></svg></span></div>
  <div class="features">
    <div class="feat blue f1"><svg viewBox="0 0 34 34"><circle cx="17" cy="17" r="14" fill="none" stroke="#fff" stroke-width="2.5"/><circle cx="17" cy="17" r="6" fill="none" stroke="#fff" stroke-width="2.5"/></svg>Proper Planing &amp;<br>Interface</div>
    <div class="feat f2"><svg viewBox="0 0 34 34"><rect x="4" y="8" width="20" height="20" fill="none" stroke="#333" stroke-width="2"/><path d="M14 22l2-6 12-12 4 4-12 12z" fill="none" stroke="#333" stroke-width="2"/></svg>Accurate<br>Monitoring</div>
    <div class="feat f3"><svg viewBox="0 0 34 34"><circle cx="17" cy="10" r="5" fill="#333"/><circle cx="7" cy="14" r="4" fill="#333"/><circle cx="27" cy="14" r="4" fill="#333"/><path d="M9 30a8 8 0 0 1 16 0zM1 28a6 6 0 0 1 10-4M33 28a6 6 0 0 0-10-4" fill="#333"/></svg>Protecting Business<br>Data</div>
    <div class="feat green f4"><svg viewBox="0 0 34 34"><path d="M17 3a9 9 0 0 0-5 16.5V24h10v-4.5A9 9 0 0 0 17 3z" fill="none" stroke="#fff" stroke-width="2.5"/><path d="M12 28h10M14 31h6" stroke="#fff" stroke-width="2.5"/></svg>Test<br>&amp; Deliver</div>
    <div class="hub"><span><svg viewBox="0 0 24 24"><ellipse cx="12" cy="5" rx="8" ry="3" fill="#fff"/><path d="M4 8c0 1.7 3.6 3 8 3s8-1.3 8-3v4c0 1.7-3.6 3-8 3s-8-1.3-8-3zM4 14c0 1.7 3.6 3 8 3s8-1.3 8-3v4c0 1.7-3.6 3-8 3s-8-1.3-8-3z" fill="#fff"/></svg></span></div>
  </div>
</section>

<section class="products">
  <h2 class="sec-title" style="top:50px">Products &amp; Services</h2>
  <p class="sec-sub" style="top:110px;left:320px;width:560px">Lorem ipsum dolor sit amet, consectetur adipiscing elit. Nulla blandit, nibh in consequat porttitor, nulla magna tincidunt augue</p>
  <div class="cards">
    <div class="card"><div class="ph" role="img" aria-label="Hands working on a laptop at a desk" style="background:linear-gradient(150deg,#d8d6d2,#8f8a84)"></div><div class="bar blue">Database Design</div></div>
    <div class="card"><div class="ph" role="img" aria-label="Blue cloud over a circuit board" style="background:radial-gradient(circle at 50% 45%,#3fa0e0,#0b3a7a 70%)"></div><div class="bar green">Data Resiliency</div></div>
    <div class="card"><div class="ph" role="img" aria-label="Team reviewing charts on a table" style="background:linear-gradient(150deg,#f2f0ec,#b5aea4)"></div><div class="bar blue">Troubleshooting</div></div>
    <div class="card"><div class="ph" role="img" aria-label="Person working at a laptop with papers" style="background:linear-gradient(150deg,#7a7068,#3f3a35)"></div><div class="bar green">Monitoring</div></div>
  </div>
  <span class="circ-arrow" style="left:125px;top:298px"><svg viewBox="0 0 8 8"><path d="M5.5 1L2.5 4l3 3" fill="none" stroke="#999" stroke-width="1.3"/></svg></span>
  <span class="circ-arrow" style="left:1063px;top:298px"><svg viewBox="0 0 8 8"><path d="M2.5 1l3 3-3 3" fill="none" stroke="#999" stroke-width="1.3"/></svg></span>
</section>

<section class="experience">
  <div class="ph" role="img" aria-label="Colleagues talking in an office, darkened"></div>
  <h2>WE HAVE 15 YEARS EXPERIENCE IN DATABASE MANAGEMANT</h2>
  <div class="tag">Transform the way you do business</div>
  <div class="phone">1800.555.0198</div>
  <div class="btn-outline"><span class="label">Contact Us</span><span class="go"><svg viewBox="0 0 10 10"><path d="M3 1l4 4-4 4" fill="none" stroke="#fff" stroke-width="1.6"/></svg></span></div>
</section>

<section class="blog">
  <h2 class="sec-title" style="top:44px">LATEST BLOG</h2>
  <p class="sec-sub" style="top:110px;left:300px;width:600px">Industry-leading companies have come to rely upon Quillbay for effective technical content. Below is a partial list of companies that engage Quillbay for their technical content needs.</p>
  <div class="posts">
    <article class="post"><div class="ph" role="img" aria-label="Hands using a tablet with data screens" style="background:linear-gradient(150deg,#2a4c7a,#0f1f36)"></div><div class="body"><h3>Advantage to handle DBA remotely</h3><div class="date"><i></i>18 MAY, 2018</div><p>Lorem ipsum dolor sit amet, consectetur adipiscing elit. Nulla blandit, nibh in consequat porttitor, nulla magna tincidunt augue, at aliquet sem est.</p><div class="more">READ MORE</div></div></article>
    <article class="post"><div class="ph" role="img" aria-label="Glowing digital globe" style="background:radial-gradient(circle at 50% 50%,#2f6fa8,#081a30 70%)"></div><div class="body"><h3>Data is about to access anywhere</h3><div class="date"><i></i>18 MAY, 2018</div><p>Lorem ipsum dolor sit amet, consectetur adipiscing elit. Nulla blandit, nibh in consequat porttitor, nulla magna tincidunt augue, at aliquet sem est.</p><div class="more">READ MORE</div></div></article>
    <article class="post"><div class="ph" role="img" aria-label="Business people pointing at reports" style="background:linear-gradient(150deg,#c9ccd0,#6e7680)"></div><div class="body"><h3>DBA solves many prolem</h3><div class="date"><i></i>18 MAY, 2018</div><p>Lorem ipsum dolor sit amet, consectetur adipiscing elit. Nulla blandit, nibh in consequat porttitor, nulla magna tincidunt augue, at aliquet sem est.</p><div class="more">READ MORE</div></div></article>
  </div>
  <div class="dots"><i class="on"></i><i></i><i></i></div>
</section>

<section class="testimonial">
  <svg class="quote" viewBox="0 0 44 36"><path d="M2 36V20C2 9 8 2 18 0v6c-5 2-8 6-8 12h8v18zM26 36V20C26 9 32 2 42 0v6c-5 2-8 6-8 12h8v18z" fill="#6aa62a"/></svg>
  <blockquote>Lorem ipsum dolor sit amet, consectetur adipiscing elit. Aliquam semper felis placerat nisi dapibus tristique. Ut semper ipsum nec nisi ullamcorper, a tincidunt massa efficitur. Aliquam ornare justo sit amet elementum tristique.</blockquote>
  <svg class="arr" style="left:220px" viewBox="0 0 20 20"><path d="M18 10H3M9 4l-6 6 6 6" fill="none" stroke="#555" stroke-width="1.6"/></svg>
  <svg class="arr" style="left:960px" viewBox="0 0 20 20"><path d="M2 10h15M11 4l6 6-6 6" fill="none" stroke="#555" stroke-width="1.6"/></svg>
  <div class="avatar" role="img" aria-label="Portrait of the client"></div>
  <div class="name">Tomas Verin</div>
  <div class="role">Manager</div>
</section>

<section class="team">
  <div class="member">
    <div class="ph" role="img" aria-label="Portrait of the project manager in a grey sweater"></div>
    <h3>MAREK DOLAN</h3>
    <div class="pos">Project Manager</div>
    <p>In vitae mauris et mauris faucibus faucibus pretium ac mi. Vestibulum eget placerat nibh. Pellentesque vulputate cursus velit ac tincidunt. Mauris elementum vitae eros ac auctor.</p>
    <div class="contact">Phone : +420 555 010 200<br>E-mail : marek.dolan@brivolan.cz</div>
    <div class="soc"><i></i><i></i></div>
    <div class="pager"><span><svg viewBox="0 0 8 8"><path d="M5.5 1L2.5 4l3 3" fill="none" stroke="#0d57a7" stroke-width="1.4"/></svg></span><span><svg viewBox="0 0 8 8"><path d="M2.5 1l3 3-3 3" fill="none" stroke="#0d57a7" stroke-width="1.4"/></svg></span></div>
  </div>
</section>

<section class="downloads">
  <div class="dl-side">
    <div class="dl" style="top:64px"><svg viewBox="0 0 70 86"><path d="M8 2h38l16 16v44H8z" fill="none" stroke="#fff" stroke-width="3"/><rect x="2" y="22" width="52" height="24" fill="#fff"/><text x="28" y="40" text-anchor="middle" font-family="Montserrat,sans-serif" font-weight="700" font-size="17" fill="#0d57a7">PDF</text><path d="M35 62v18M27 72l8 8 8-8" fill="none" stroke="#fff" stroke-width="3"/></svg>DOWNLOAD FILES</div>
    <div class="dl" style="top:256px"><svg viewBox="0 0 70 86"><path d="M8 2h38l16 16v44H8z" fill="none" stroke="#fff" stroke-width="3"/><rect x="2" y="22" width="52" height="24" fill="#fff"/><text x="28" y="40" text-anchor="middle" font-family="Montserrat,sans-serif" font-weight="700" font-size="17" fill="#0d57a7">PPT</text><path d="M35 62v18M27 72l8 8 8-8" fill="none" stroke="#fff" stroke-width="3"/></svg>DOWNLOAD PPTs</div>
  </div>
  <div class="talk-side">
    <h2>Start a Discussion</h2>
    <div class="field" style="left:54px;top:122px;width:180px">Your Name</div>
    <div class="field" style="left:248px;top:122px;width:177px">Your Email Address</div>
    <div class="field" style="left:54px;top:170px;width:180px">Phone Number</div>
    <div class="field" style="left:248px;top:170px;width:177px">Company</div>
    <div class="field" style="left:54px;top:214px;width:371px;height:80px">Message</div>
    <div class="submit"><span class="label">Submit Now</span><span class="go"><svg viewBox="0 0 10 10"><path d="M3 1l4 4-4 4" fill="none" stroke="#fff" stroke-width="1.6"/></svg></span></div>
  </div>
</section>

<footer class="site-footer">
  <div class="brand"><span class="mark"></span>BRIVOLAN</div>
  <div class="f-phone">1800.555.0198</div>
  <p class="f-addr">A 120 Lorem ipsum dolor sit amet,<br>consectetur.<br>hello@brivolan.cz</p>
  <div class="f-head" style="left:482px">Services</div>
  <ul class="f-list" style="left:482px"><li>Database design</li><li>Administrating</li><li>Data Resiliency</li><li>Troubleshooting</li><li>Monitoring</li></ul>
  <ul class="f-list" style="left:607px"><li>Database design</li><li>Administrating</li><li>Data Resiliency</li><li>Troubleshooting</li><li>Monitoring</li></ul>
  <div class="f-head" style="left:813px">Newsletter</div>
  <div class="f-news">Get latest updates and offers.</div>
  <div class="f-email">Email Address<span><svg viewBox="0 0 14 14"><path d="M1 7l12-6-4 12-2-5z" fill="#fff"/></svg></span></div>
  <div class="f-soc"><i></i><i></i><i></i><i></i><i></i></div>
  <div class="f-bottom"><span>Copyright 2018 BRIVOLAN | All Rights Reserved</span><span>Terms and Condition | Privacy Policy</span></div>
  <div class="to-top"><svg viewBox="0 0 10 10"><path d="M1 7l4-4 4 4" fill="none" stroke="#fff" stroke-width="1.6"/></svg></div>
</footer>

</body>
</html>
```